Business Card Design for Engineering Firm

Need a business card design for small mechanical and plumbing engineering form based in Utah. Design should be customizable for all employees.

```html
<!DOCTYPE html>
<html lang="en">
<head>
<meta charset="UTF-8">
<title>Larkspur Engineering — Business Cards</title>
<link rel="stylesheet" href="https://fonts.googleapis.com/css2?family=Open+Sans:wght@400;600&family=Crimson+Text:wght@700&display=swap">
<style>
  :root {
    --bg: #e4e5e8;
    --card: #ffffff;
    --brand-red: #8a0f14;
    --text-grey: #4a4a4a;
    --rule-grey: #8c8c8c;
  }
  * { margin: 0; padding: 0; box-sizing: border-box; }
  html, body { width: 1200px; height: 800px; overflow: hidden; }
  body {
    background: var(--bg);
    font-family: "Open Sans", sans-serif;
    display: flex;
    align-items: center;
    justify-content: center;
    gap: 60px;
  }
  .card {
    position: relative;
    width: 520px;
    height: 297px;
    background: var(--card);
    box-shadow: 0 6px 18px rgba(0,0,0,0.12);
    overflow: hidden;
  }
  .card__band {
    position: absolute;
    left: 0; right: 0;
    bottom: 10px;
    height: 11px;
    background: var(--brand-red);
  }
  /* Front side */
  .front__wordmark {
    position: absolute;
    left: 0; right: 0;
    top: 120px;
    text-align: center;
    color: var(--brand-red);
    font-weight: 400;
    line-height: 1.1;
  }
  .wordmark__name { display: block; font-size: 40px; letter-spacing: 2px; }
  .wordmark__sub { display: block; font-size: 15px; letter-spacing: 10px; }

  /* Back side */
  .contact__person {
    position: absolute;
    left: 34px; top: 30px;
  }
  .person__name {
    font-family: "Crimson Text", serif;
    font-weight: 700;
    color: var(--brand-red);
    font-size: 17px;
    letter-spacing: 0.5px;
  }
  .person__title { font-size: 12px; color: var(--text-grey); margin-top: -2px; }
  .contact__rule {
    position: absolute;
    left: 34px; right: 30px;
    top: 78px;
    border-top: 1px solid var(--rule-grey);
  }
  .contact__list {
    position: absolute;
    left: 34px; top: 90px;
    list-style: none;
    font-size: 12.5px;
    color: var(--text-grey);
    line-height: 20px;
  }
  .contact__list li { display: flex; align-items: center; gap: 8px; }
  .contact__list svg { width: 12px; height: 12px; fill: var(--brand-red); flex: none; }
  .back__wordmark {
    position: absolute;
    right: 30px; top: 112px;
    text-align: right;
    color: var(--brand-red);
    font-weight: 400;
    line-height: 1.15;
  }
  .back__wordmark .wordmark__name { font-size: 30px; letter-spacing: 1.5px; }
  .back__wordmark .wordmark__sub { font-size: 12px; letter-spacing: 8px; }
  .contact__address {
    position: absolute;
    right: 30px; bottom: 36px;
    text-align: right;
    font-size: 13px;
    color: var(--text-grey);
    line-height: 17px;
  }
</style>
</head>
<body>
  <section class="card card--front" aria-label="Card front">
    <h1 class="front__wordmark">
      <span class="wordmark__name">LARKSPUR</span>
      <span class="wordmark__sub">ENGINEERING</span>
    </h1>
    <div class="card__band"></div>
  </section>

  <section class="card card--back" aria-label="Card back">
    <div class="contact__person">
      <p class="person__name">DANA PORTER</p>
      <p class="person__title">Director</p>
    </div>
    <div class="contact__rule"></div>
    <ul class="contact__list">
      <li><svg viewBox="0 0 12 12"><path d="M3 0h6a1 1 0 0 1 1 1v10a1 1 0 0 1-1 1H3a1 1 0 0 1-1-1V1a1 1 0 0 1 1-1zm0 1.5v8h6v-8z"/></svg>300-555-0142</li>
      <li><svg viewBox="0 0 12 12"><path d="M2.5 0.5l2 2.5-1.2 1.5a7 7 0 0 0 4.2 4.2L9 7.5l2.5 2-1.3 2A10 10 0 0 1 0.5 1.8z"/></svg>300-555-0142</li>
      <li><svg viewBox="0 0 12 12"><path d="M0 2h12v8H0zm1 1v.4l5 3.1 5-3.1V3zm0 1.6V9h10V4.6L6 7.7z"/></svg>info@larkspurengineering.com</li>
      <li><svg viewBox="0 0 12 12"><path d="M6 0a6 6 0 1 1 0 12A6 6 0 0 1 6 0zm0 1.3a4.7 4.7 0 1 0 0 9.4 4.7 4.7 0 0 0 0-9.4zM5.4 3h1.2v5H5.4z"/></svg>www.larkspurengineering.com</li>
    </ul>
    <p class="back__wordmark">
      <span class="wordmark__name">LARKSPUR</span>
      <span class="wordmark__sub">ENGINEERING</span>
    </p>
    <address class="contact__address" style="font-style:normal">
      99 sample street<br>sample city 0000
    </address>
    <div class="card__band"></div>
  </section>
</body>
</html>
```